Firm of surveyors needs a professional yet friendly looking flyer

Our company offers help to landlords who have a phone mast on their property. We help them to negotiate the best rent and lease terms. There are so many landlords who don't seek professional advice because they don't know it's available. We want to send them a flyer which is informative, looks professional but also friendly so it prompts them to call us. I have attached the wording and some pictures but have more I can send but they were too large to attach.

Target Market(s)

Ranges from farmers to large corporations and land owners

Industry/Entity Type

Surveyor

Font styles to use
Sans Serif

Colors
acd136
9bcb3c
000000
ffffff
606060
848484

Requirements
Must have
• Must be clear, must give a professional look, must include pictures, must include our logo, must use our colour scheme (or variations of it). Ideally, I would like a try-fold design if possible.
Nice to have
• I would like there to be stand out lines to catch the readers eye (I have included some on the wording document). I would like a clean and modern design
Should not have
• Should not be too fussy

```html
<!DOCTYPE html>
<html lang="en">
<head>
<meta charset="utf-8">
<title>Mastwise Lease Advisors – Tri-fold Flyer</title>
<link href="https://fonts.googleapis.com/css2?family=Montserrat:ital,wght@0,300;0,400;0,600;0,700;1,700&display=swap" rel="stylesheet">
<style>
  :root{
    --lime:#acd136;
    --green:#9bcb3c;
    --forest:#3b5f45;
    --forest-dark:#2d4a36;
    --ink:#000000;
    --white:#ffffff;
    --charcoal:#333333;
    --grey:#606060;
    --grey-light:#848484;
    --stage:#e4e4e4;
    --sky:#3f73c4;
  }
  *{box-sizing:border-box;margin:0;padding:0}
  html,body{width:1200px;height:798px;overflow:hidden}
  body{background:var(--stage);font-family:"Montserrat",Arial,sans-serif;color:var(--grey);position:relative}
  .spread{position:absolute;top:200px;width:564px;height:398px;display:flex;box-shadow:0 6px 18px rgba(0,0,0,.18)}
  .spread--outside{left:24px}
  .spread--inside{left:612px}
  .panel{position:relative;width:188px;height:100%;background:var(--white);overflow:hidden}
  .panel + .panel{border-left:1px solid #ececec}
  .heading{color:var(--green);font-weight:700;text-transform:uppercase;font-size:9.5px;line-height:1.25;letter-spacing:.2px}
  .body-copy{font-size:6.6px;line-height:1.5;color:var(--grey)}
  .body-copy + .body-copy{margin-top:6px}
  .callout{color:var(--green);font-weight:700;text-transform:uppercase;font-size:7.4px;line-height:1.3;margin-top:7px}
  .photo{position:absolute;left:0;width:100%}
  .stripes{position:absolute;left:0;width:100%}
  /* about panel */
  .about__text{padding:18px 16px 0}
  .about__text .heading{margin-bottom:8px}
  .about .photo{bottom:0;height:110px;background:linear-gradient(160deg,#5b8fd9,#2f5fae)}
  .about .stripes{bottom:92px;height:50px}
  /* contact panel */
  .contact__hero{position:absolute;top:0;left:0;width:100%;height:190px;background:linear-gradient(180deg,var(--forest) 0%,var(--forest-dark) 100%)}
  .contact__title{position:absolute;top:34px;left:0;width:100%;text-align:center;font-weight:300;font-size:27px;line-height:1.05;letter-spacing:1px;color:var(--white);text-transform:uppercase}
  .contact__title .accent{color:var(--lime)}
  .contact__curve{position:absolute;top:150px;left:0;width:100%;height:60px}
  .contact__list{position:absolute;top:200px;left:16px;right:10px;list-style:none}
  .contact__item{display:flex;align-items:flex-start;gap:8px;margin-bottom:11px}
  .contact__icon{flex:0 0 16px;height:16px;border-radius:50%;background:var(--lime);display:flex;align-items:center;justify-content:center}
  .contact__label{font-size:7px;font-weight:700;color:var(--charcoal);text-transform:uppercase}
  .contact__value{font-size:6.4px;line-height:1.35;color:var(--grey)}
  /* cover */
  .cover__art{position:absolute;left:0;top:0;width:188px;height:398px}
  .cover__brand{position:absolute;left:64px;top:183px;display:flex;align-items:center;gap:5px}
  .cover__mark{width:8px;height:8px;border-radius:50%;background:var(--green);flex:0 0 8px}
  .cover__name{font-size:9px;font-weight:700;color:var(--green);text-transform:uppercase;line-height:1.2;white-space:nowrap}
  .cover__prompt{position:absolute;left:20px;right:18px;bottom:22px;font-size:9.5px;line-height:1.35;font-weight:700;font-style:italic;color:var(--green)}
  .cover__prompt span{display:block;color:var(--grey-light);font-style:normal;font-weight:600;font-size:8px;margin-bottom:2px}
  /* inside */
  .landscape .photo{top:0;height:230px;background:linear-gradient(180deg,#8fb9ec 0%,#cfe0f3 55%,#7c9a52 78%,#5d7a3a 100%)}
  .landscape .stripes{top:205px;height:80px}
  .landscape__text{position:absolute;top:290px;left:16px;right:14px}
  .climate{padding:18px 16px}
  .climate .heading{margin-bottom:8px}
  .advertise .photo{top:0;height:200px;background:linear-gradient(200deg,#6b9ee6 0%,var(--sky) 100%)}
  .advertise .stripes{top:170px;height:60px}
  .advertise__text{position:absolute;top:250px;left:16px;right:14px}
</style>
</head>
<body>

<section class="spread spread--outside" aria-label="Flyer outside">
  <article class="panel about">
    <div class="about__text">
      <h2 class="heading">Mastwise Lease Advisors is a firm of surveyors experienced in mobile phone masts</h2>
      <p class="body-copy">We have built up a wealth of knowledge over thousands of mast deals across the country. Our telecoms team are chartered surveyors who have worked for mast operators and now act exclusively for landowners, ensuring you receive fair rent and the best lease terms in place.</p>
      <p class="body-copy">Many of these leases are now up for renewal. We are here to help.</p>
      <p class="callout">We are currently offering free lease reviews and recommendations</p>
    </div>
    <svg class="stripes" viewBox="0 0 188 50" preserveAspectRatio="none" aria-hidden="true">
      <polygon points="0,34 188,14 188,28 0,48" fill="var(--charcoal)"/>
      <polygon points="70,12 188,0 188,6 70,18" fill="var(--lime)"/>
    </svg>
    <div class="photo" role="img" aria-label="Photograph of a mobile phone mast against blue sky"></div>
  </article>

  <article class="panel contact">
    <div class="contact__hero" role="img" aria-label="Green-tinted photograph of a phone mast"></div>
    <h2 class="contact__title">Get<br>in<br><span class="accent">Touch</span></h2>
    <svg class="contact__curve" viewBox="0 0 188 60" preserveAspectRatio="none" aria-hidden="true">
      <path d="M0 40 Q94 -10 188 25 L188 60 L0 60 Z" fill="var(--white)"/>
    </svg>
    <ul class="contact__list">
      <li class="contact__item">
        <span class="contact__icon"><svg width="8" height="8" viewBox="0 0 10 10"><path d="M5 0.5a3.2 3.2 0 0 0-3.2 3.2C1.8 6 5 9.5 5 9.5S8.2 6 8.2 3.7A3.2 3.2 0 0 0 5 .5z" fill="#fff"/></svg></span>
        <div><div class="contact__label">Address</div><div class="contact__value">Mastwise Lease Advisors Ltd, Unit 4 Meadow Court, Elmbridge Farm Estate, Shropshire SY9 2QT</div></div>
      </li>
      <li class="contact__item">
        <span class="contact__icon"><svg width="8" height="8" viewBox="0 0 10 10"><path d="M2 .8l1.8 2-1 1.2a6 6 0 0 0 3.2 3.2l1.2-1 2 1.8-1.2 1.6C4.5 9.2.8 5.5.4 2z" fill="#fff"/></svg></span>
        <div><div class="contact__label">Phone</div><div class="contact__value">01632 960418</div></div>
      </li>
      <li class="contact__item">
        <span class="contact__icon"><svg width="8" height="8" viewBox="0 0 10 10"><rect x="1" y="3" width="8" height="5" fill="#fff"/><rect x="3" y="1" width="4" height="2" fill="#fff"/></svg></span>
        <div><div class="contact__label">Fax Number</div><div class="contact__value">01632 960419</div></div>
      </li>
      <li class="contact__item">
        <span class="contact__icon"><svg width="8" height="8" viewBox="0 0 10 10"><rect x="1" y="2" width="8" height="6" fill="#fff"/><path d="M1 2l4 3.5L9 2" stroke="var(--lime)" fill="none"/></svg></span>
        <div><div class="contact__label">Email</div><div class="contact__value">hello@mastwiseadvisors.co.uk</div></div>
      </li>
      <li class="contact__item">
        <span class="contact__icon"><svg width="8" height="8" viewBox="0 0 10 10"><circle cx="5" cy="5" r="4" stroke="#fff" fill="none"/><path d="M1 5h8M5 1v8" stroke="#fff"/></svg></span>
        <div><div class="contact__label">Website</div><div class="contact__value">www.mastwiseadvisors.co.uk</div></div>
      </li>
    </ul>
  </article>

  <article class="panel cover">
    <svg class="cover__art" viewBox="0 0 188 398" aria-hidden="true">
      <polygon points="0,0 188,0 188,60 0,120" fill="var(--charcoal)"/>
      <polygon points="0,120 188,60 188,78 0,138" fill="var(--forest)"/>
      <polygon points="0,146 188,86 188,92 0,152" fill="var(--lime)"/>
      <polygon points="8,160 184,100 154,310" fill="none" stroke="var(--green)" stroke-width="4.5" stroke-linejoin="miter"/>
    </svg>
    <div class="cover__brand">
      <span class="cover__mark"></span>
      <span class="cover__name">Mastwise<br>Lease Advisors</span>
    </div>
    <p class="cover__prompt"><span>Unsure whether you are getting the best rent?</span>Call us now for a free, no obligation chat</p>
  </article>
</section>

<section class="spread spread--inside" aria-label="Flyer inside">
  <article class="panel landscape">
    <div class="photo" role="img" aria-label="Photograph of a lattice phone mast on a green hillside under a cloudy sky"></div>
    <svg class="stripes" viewBox="0 0 188 80" preserveAspectRatio="none" aria-hidden="true">
      <polygon points="0,50 188,0 188,40 0,80" fill="var(--charcoal)"/>
      <polygon points="0,80 188,40 188,80 0,80" fill="var(--white)"/>
    </svg>
    <div class="landscape__text">
      <p class="body-copy">Whether you own a farm, an estate or a commercial building, a mast on your land is a valuable asset. We make sure it is treated like one.</p>
    </div>
  </article>

  <article class="panel climate">
    <h2 class="heading">Current telecoms climate</h2>
    <p class="body-copy">The telecoms market, in relation to mobile phone masts, is going through some huge changes. Operators are combining to cut costs and share sites, and several networks have merged or formed jointly owned companies. What this can mean for the landowner is pressure on their site and potentially their rent. It can all be very confusing, but this is where we can help. We know the industry and understand how a merger may affect a landlord, therefore we provide the best advice on protecting your asset.</p>
    <p class="body-copy">In 2017 the Government introduced the Digital Economy Act. This sets out significant changes for landlords, including the way rents are valued. We have already seen operators use the code, trying to reduce their rent in line with the new law. We are working alongside specialist telecoms solicitors to reduce any potential negative impact on landlords.</p>
    <p class="callout">Landlords should not sign anything until they have sought professional advice</p>
  </article>

  <article class="panel advertise">
    <div class="photo" role="img" aria-label="Photograph of antennas on a steel mast against blue sky"></div>
    <svg class="stripes" viewBox="0 0 188 60" preserveAspectRatio="none" aria-hidden="true">
      <polygon points="0,40 188,0 188,24 0,60" fill="var(--charcoal)"/>
      <polygon points="0,60 188,24 188,60" fill="var(--white)"/>
      <polygon points="0,52 120,28 120,33 0,57" fill="var(--lime)"/>
    </svg>
    <div class="advertise__text">
      <p class="body-copy">If you are interested in having a mast on your land, we can help you find an operator. Advertise your site on our website to take advantage of this service.</p>
    </div>
  </article>
</section>

</body>
</html>
```